Meadowlark Lane Yoga Facebook Design

"Practice Radiant Movement"

Foundational and sustainable yoga practice to cultivate growth through a variety of anatomy- informed movement patterns. Develop an informative and inspirational connection with the mind, body and spirit, through smart and integrated movement.

-I need a design that is happy and cheerful and attracts children and adults alike. I teach vinyassa based yoga that is sustainable and smart, kid yoga, and chair yoga.

-A movement practic rooted in foundation, core, and expression

- Accessible yoga for a sustained practice. A guided movement practice where one gains information and knowledge of oneself through a mind/body connection. For one feel good physically with a new awareness of their internal radiance that exists in all beings. Physical rejuvenation egnites a light and increases energy to flow through the physical body, which ultimately tranlates into works of kindness for others and out in the world.

Nora Whitfield
Yoga Instructor
MD, Pediatrician
RYT-200
RCYT
Certified yoga teacher for adults and children

Full description:
What is the positioning or mission statement of your company? to guide individuals in a yoga-based safe and sustainable movement practice applicable to all ages and body types. Currently my focus is working with children in daycare and school settings, but my goal is to expand into private yoga practice for adults, and potentially as part of rented space in studios. I hope to find a way to work with children AND adults (so would love for logo to be appealing to both), but current focus is with children based on need and demand in the community. yoga for children also compliments my backround as a pediatrician/neonatologist, and I greatly miss interacting with children. I also want to emphasize a yoga/movement practice that is focused more on what one feels internally through movement. NOT what one looks like asthetically. I believe in removing all mirrors from yoga/movement practice. It should be an experience of movement/poses/yoga through appropriate cueing and education. It is not about the details of how far the knee should bend, or how high the leg should be. Focusing on foudation first, core, then core engagement and ultimately expression of poses/movements. A focus on strength, stability and mobility, not just flexibility, which is the common perception/association with yoga. I also want individuals to learn to be an advocate of their own health. Through guidance, I hope for individuals to connect with their body so they know themselves so well to be able to advocate for themselves in the modern healthcare world. This internal experience and connection is so essential in a world where modern medicine has become a business and it is all about making a dollar. the connection with patients is lost, and individuals need to learn to empower themselves and through their new found voice to be able to articulate what is wrong.
Does your company have a tagline or slogan that should be included with the logo? "Practice Radiant Movement"
What do you hope your company can be known for? Accessible yoga for a sustained practice. A guided movement practice where one gains information and knowledge of oneself through a mind/body connection. For one feel good physically with a new awareness of their internal radiance that exists in all beings. Physical rejuvenation egnites a light and increases energy to flow through the physical body, which ultimately tranlates into works of kindness for others and out in the world.
What color palettes might you prefer? why? love the colors currently chosen
Where will the logo be primarily used? initially business cards, but hopefully future websites, t-shirts, and potentially local magazine adds. Also starting with a small couple of banners for community events in the area. I currently practice as a nomad out of my car :)
Are there any elements you would prefer to see in the logo? Movement. A modern depiction of a human body/figure practicing movement. Hoping to avoid a stereotypical yoga pose per say, just because I want to people to think of it more of a movement practice with yoga roots. Modern yoga. There are elements of breathing and connecting with oneself through the flow of breath and movement, but I do not focus on the meditative/cerebral aspect of the yoga practice. What I teach is almost reaching a meditative state through movement. I personally don't practice, nor resonate with just seated meditation. just not my thing :)
In your opinion, what defines a well-designed logo? curiosity. enough info for individuals to think they know what it means, but want to know more. invokes curiosity, but not too abstract. Reproducible. not too complicated. I want also to invoke a community feel, so a design that appeals to all people within a community.
What is your preference in reference to icons, typography, spokespeople (characters), etc.? modern design. I love the idea of a logo for my purposes, to invoke a sense of movement from within. So not too static.
What words or icons must be included in the logo? movement with yoga roots.
What logos do you like and why? A representation, but not exact. I think some ambiguity is intriguing for others, and also memorable. I want it to be an artistic representation of movement/yoga
What logos do you dislike and why? too busy, too loud.
In your opinion, what is the primary purpose for a logo? association
Who is the primary target audience? (who is most likely to use your services/product?) Children and their parents, but ultimately to expand into teaching adults. I even have aspirations of prenatal and post-natal yoga. Potentially incorporating infants.
Who currently uses your product the most? n/a (working in schools/daycare currently. It is currently all volunteer)
Are you pleased with the range of people your company serves? n/a
Are you looking to expand, modify, or completely change your target audience? or will it remain the same? yes! expand into an adult audience.
How do you plan to focus on your target audience? currently by working through schools and daycares. hopefully ultimately through after school care programs and then offering kid yoga in an existing yoga studio (working on this with Q studio in Ridgeland, currently)
What are your main forms of advertising? word of mouth, schools, daycares. Happy kids talking to their parents about the yoga class they took and happy teachers :)
How do most customers find out about your company?
Which gender are you targeting? All genders! However, with kid yoga, often the maternal individual in the child's life is more involved with decision making as far as extracurricular activities

Target Market(s)

Adults, children and families interested in movement, wellness and fun

Font styles to use
Sans Serif

Requirements
Must have
• ***I meant to emphasize the that "S" figure in my logo is SOOO iimportant to me. My daughter designed it. please highlight the "S" figure if possible******
My logo and the phrase "practice radiant movement"
Same colors as my logo
Feel like movement and fun.
Attracts children and families
Incorporate pieces of my description somehow
Nice to have
• different yoga poses or figures in movement
abstract design
attacts all body types and genders
inclusive

Industry is yoga, movement, wellness
Should not have
• no darkness
want happy and vibrant, inviting

```html
<!DOCTYPE html>
<html lang="en">
<head>
<meta charset="utf-8">
<title>Meadowlark Lane Yoga – Facebook Ad Layouts</title>
<link rel="stylesheet" href="https://fonts.googleapis.com/css2?family=Montserrat:wght@500;700&family=Great+Vibes&family=Cormorant+SC:wght@600&family=Alegreya+SC&display=swap">
<style>
  :root {
    --page: #ffffff;
    --ink: #1f1f1f;
    --white-text: #ffffff;
    --text-glow: rgba(70, 52, 34, 0.6);
    --text-halo: rgba(70, 52, 34, 0.35);
    --sun: #f2c21a;
    --teal: #2aa8bb;
  }
  * { box-sizing: border-box; margin: 0; padding: 0; }
  html, body {
    width: 1200px; height: 1200px; overflow: hidden;
    background: var(--page);
  }
  .board {
    position: relative; width: 1200px; height: 1200px;
    font-family: "Montserrat", sans-serif; color: var(--ink);
  }
  .board-title {
    position: absolute; top: 34px; left: 0; width: 100%;
    text-align: center; font-weight: 700; font-size: 24px; letter-spacing: 1.5px;
  }
  .board-size {
    position: absolute; top: 64px; left: 0; width: 100%;
    text-align: center; font-weight: 500; font-size: 23px; letter-spacing: 1px;
  }
  .layout-label {
    position: absolute; width: 535px; text-align: center;
    font-weight: 700; font-size: 15px; letter-spacing: 1px;
  }
  .ad {
    position: absolute; width: 535px; height: 280px; overflow: hidden;
  }
  .ad-photo { position: absolute; inset: 0; }
  .ad-corner { position: absolute; right: 0; bottom: 0; width: 110px; height: 110px; }
  .brand {
    position: absolute; left: 22px; top: 30px;
    display: flex; align-items: center; gap: 6px;
  }
  .brand-dot {
    width: 44px; height: 44px; border-radius: 50%; background: var(--sun); opacity: 0.9;
  }
  .brand-name {
    font-family: "Alegreya SC", serif; font-size: 15px; color: var(--teal);
    line-height: 1.05; width: 90px;
  }
  .brand.bottom { top: auto; bottom: 30px; left: 14px; }
  .tagline {
    position: absolute; left: 0; width: 100%; top: 124px;
    text-align: center; font-family: "Great Vibes", cursive; font-size: 52px; line-height: 1;
    color: var(--white-text); white-space: nowrap;
    text-shadow: 0 1px 3px var(--text-glow);
  }
  .instructor {
    position: absolute; left: 0; width: 100%; top: 199px;
    text-align: center; font-family: "Cormorant SC", serif; font-weight: 600;
    font-size: 13px; line-height: 13px; letter-spacing: 3px; color: var(--white-text);
    text-shadow: 0 1px 2px var(--text-glow), 0 0 6px var(--text-halo);
  }
  .credential {
    position: absolute; left: 0; width: 100%; top: 245px;
    text-align: center; font-family: "Cormorant SC", serif; font-weight: 600;
    font-size: 10px; letter-spacing: 0.3px; color: var(--white-text);
    text-shadow: 0 1px 2px var(--text-glow), 0 0 5px var(--text-halo);
  }
  .col-left { left: 47px; }
  .col-right { left: 618px; }
</style>
</head>
<body>
<main class="board">
  <h1 class="board-title">FACEBOOK AD DESIGN</h1>
  <p class="board-size">1200X628</p>

  <h2 class="layout-label col-left" style="top:128px">LAYOUT 01</h2>
  <section class="ad col-left" style="top:155px">
    <div class="ad-photo" role="img" aria-label="Photo of a woman in a seated forward fold on a galaxy-print mat on a wooden floor" style="background:linear-gradient(135deg,#c2ad8e 0%,#b09a7c 35%,#8a7f7a 55%,#cdb99a 80%,#e2d5bd 100%)"></div>
    <svg class="ad-corner" viewBox="0 0 110 110"><polygon points="110,0 110,110 0,110" fill="#fff" fill-opacity="0.35"/></svg>
    <div class="brand"><span class="brand-dot"></span><span class="brand-name">Meadowlark Lane Yoga</span></div>
    <p class="tagline">Practice radiant movement</p>
    <p class="instructor">NORA WHITFIELD<br>YOGA INSTRUCTOR</p>
    <p class="credential">CERTIFIED YOGA TEACHER FOR ADULTS AND CHILDREN</p>
  </section>

  <h2 class="layout-label col-right" style="top:128px">LAYOUT 02</h2>
  <section class="ad col-right" style="top:155px">
    <div class="ad-photo" role="img" aria-label="Photo of two women kneeling with hands in prayer beside a potted palm" style="background:linear-gradient(90deg,#958a7d 0%,#cfc19b 30%,#e2d3ac 55%,#d8bc98 75%,#5f6470 100%)"></div>
    <svg class="ad-corner" viewBox="0 0 110 110"><polygon points="110,0 110,110 0,110" fill="#fff" fill-opacity="0.35"/></svg>
    <div class="brand"><span class="brand-dot"></span><span class="brand-name">Meadowlark Lane Yoga</span></div>
    <p class="tagline">Practice radiant movement</p>
    <p class="instructor">NORA WHITFIELD<br>YOGA INSTRUCTOR</p>
    <p class="credential">CERTIFIED YOGA TEACHER FOR ADULTS AND CHILDREN</p>
  </section>

  <h2 class="layout-label col-left" style="top:441px">LAYOUT 03</h2>
  <section class="ad col-left" style="top:467px">
    <div class="ad-photo" role="img" aria-label="Photo of a woman balancing in a squatting pose with arms outstretched on a yoga mat" style="background:linear-gradient(90deg,#a0967f 0%,#ddcfa6 30%,#e2d5ae 55%,#bfad93 80%,#a99c86 100%)"></div>
    <svg class="ad-corner" viewBox="0 0 110 110"><polygon points="110,0 110,110 0,110" fill="#fff" fill-opacity="0.35"/></svg>
    <div class="brand"><span class="brand-dot"></span><span class="brand-name">Meadowlark Lane Yoga</span></div>
    <p class="tagline">Practice radiant movement</p>
    <p class="instructor">NORA WHITFIELD<br>YOGA INSTRUCTOR</p>
    <p class="credential">CERTIFIED YOGA TEACHER FOR ADULTS AND CHILDREN</p>
  </section>

  <h2 class="layout-label col-right" style="top:441px">LAYOUT 04</h2>
  <section class="ad col-right" style="top:467px">
    <div class="ad-photo" role="img" aria-label="Close photo of a seated woman with hands joined in prayer" style="background:linear-gradient(90deg,#ad9373 0%,#cfa983 25%,#e6c7a2 50%,#cfa982 75%,#b19374 100%)"></div>
    <svg class="ad-corner" viewBox="0 0 110 110"><polygon points="110,0 110,110 0,110" fill="#fff" fill-opacity="0.35"/></svg>
    <div class="brand"><span class="brand-dot"></span><span class="brand-name">Meadowlark Lane Yoga</span></div>
    <p class="tagline">Practice radiant movement</p>
    <p class="instructor">NORA WHITFIELD<br>YOGA INSTRUCTOR</p>
    <p class="credential">CERTIFIED YOGA TEACHER FOR ADULTS AND CHILDREN</p>
  </section>

  <h2 class="layout-label col-left" style="top:754px">LAYOUT 05</h2>
  <section class="ad col-left" style="top:783px">
    <div class="ad-photo" role="img" aria-label="Photo of a woman in a backbend pose on a mat beside a potted palm" style="background:linear-gradient(90deg,#9c917c 0%,#d8cba4 30%,#e2d5b0 55%,#dccda7 80%,#bba98b 100%)"></div>
    <svg class="ad-corner" viewBox="0 0 110 110"><polygon points="110,0 110,110 0,110" fill="#fff" fill-opacity="0.35"/></svg>
    <div class="brand bottom"><span class="brand-dot"></span><span class="brand-name">Meadowlark Lane Yoga</span></div>
    <p class="tagline">Practice radiant movement</p>
    <p class="instructor">NORA WHITFIELD<br>YOGA INSTRUCTOR</p>
    <p class="credential">CERTIFIED YOGA TEACHER FOR ADULTS AND CHILDREN</p>
  </section>

  <h2 class="layout-label col-right" style="top:754px">LAYOUT 06</h2>
  <section class="ad col-right" style="top:783px">
    <div class="ad-photo" role="img" aria-label="Photo of a woman kneeling with hands in prayer on a mat beside candles and a palm" style="background:linear-gradient(90deg,#9b907d 0%,#d9cca5 30%,#ddcfaa 50%,#7b7a80 62%,#dccea8 78%,#bfb094 100%)"></div>
    <svg class="ad-corner" viewBox="0 0 110 110"><polygon points="110,0 110,110 0,110" fill="#fff" fill-opacity="0.35"/></svg>
    <div class="brand"><span class="brand-dot"></span><span class="brand-name">Meadowlark Lane Yoga</span></div>
    <p class="tagline">Practice radiant movement</p>
    <p class="instructor">NORA WHITFIELD<br>YOGA INSTRUCTOR</p>
    <p class="credential">CERTIFIED YOGA TEACHER FOR ADULTS AND CHILDREN</p>
  </section>
</main>
</body>
</html>
```